The Tidy Lantern Business Card

I need a business card designed for The Tidy Lantern. The company provides on site support and education to end consumers in the ins and outs of all our digital devices. We advise on product purchase, installation, maintenance and troubleshooting. Anything from cordless phones to home networks.
My initial concept is double sided with the white logo on green on one side and contact details and a small logo on the flip side (logo package attached)
Contact Details:
Miles Fenwright
Managing Director
PO Box 43
Brackton, NSW 2187
Phone: 0438 907 516
email: miles@tidylantern.com.au
web: www.tidylantern.com.au
Target Market(s)
Busy professionals and retired folks.
Industry/Entity Type
Education
Look and feel

```html
<!DOCTYPE html>
<html lang="en">
<head>
<meta charset="utf-8">
<title>The Tidy Lantern – Business Card</title>
<link rel="stylesheet" href="https://fonts.googleapis.com/css2?family=Open+Sans:wght@400;600;700&display=swap">
<style>
  :root {
    --page: #ecebe9;
    --leaf-green: #6aa93a;
    --card-white: #ffffff;
    --ink-navy: #1c2a3a;
    --ink-dark: #222222;
    --sub-white: #e6f1dc;
  }
  * { box-sizing: border-box; margin: 0; padding: 0; }
  html, body {
    width: 1200px; height: 997px; overflow: hidden;
    background: var(--page);
    font-family: "Open Sans", Arial, sans-serif;
  }
  .card-set {
    position: absolute; left: 60px; top: 330px;
    display: flex; gap: 60px;
  }
  .card {
    position: relative; width: 510px; height: 312px;
    overflow: hidden;
    box-shadow: 0 2px 6px rgba(0,0,0,0.12);
  }
  /* Front */
  .card-front { background: var(--leaf-green); color: var(--card-white); }
  .front-brand {
    position: absolute; right: 44px; top: 70px;
    display: flex; align-items: center; gap: 14px;
  }
  .brand-dot {
    width: 26px; height: 26px; border-radius: 50%;
    background: var(--card-white);
  }
  .front-brand .brand-name {
    font-weight: 600; font-size: 30px; letter-spacing: 0.5px;
  }
  .front-url {
    position: absolute; left: 36px; bottom: 34px;
    font-weight: 700; font-size: 17px;
  }
  /* Back */
  .card-back { background: var(--card-white); }
  .name-band {
    position: absolute; left: 0; top: 58px;
    width: 290px; height: 96px;
    background: var(--leaf-green);
    border-radius: 0 48px 48px 0;
    padding: 22px 0 0 60px;
  }
  .person-name {
    font-weight: 700; font-size: 18px; color: var(--ink-navy);
  }
  .person-title {
    font-size: 14px; color: var(--sub-white); margin-top: 4px;
  }
  .back-brand {
    position: absolute; right: 30px; top: 80px;
    display: flex; align-items: center; gap: 10px;
  }
  .back-brand .brand-dot { width: 18px; height: 18px; background: var(--leaf-green); }
  .back-brand .brand-name {
    font-weight: 600; font-size: 20px; color: var(--ink-navy);
  }
  .contact-list {
    position: absolute; left: 36px; bottom: 34px;
    list-style: none; font-size: 14.5px; line-height: 1.45;
    color: var(--ink-dark);
  }
</style>
</head>
<body>
  <main class="card-set">
    <section class="card card-front" aria-label="Card front">
      <div class="front-brand">
        <span class="brand-dot"></span>
        <span class="brand-name">The Tidy Lantern</span>
      </div>
      <p class="front-url">www.tidylantern.com.au</p>
    </section>

    <section class="card card-back" aria-label="Card back">
      <div class="name-band">
        <p class="person-name">Miles Fenwright</p>
        <p class="person-title">Managing Director</p>
      </div>
      <div class="back-brand">
        <span class="brand-dot"></span>
        <span class="brand-name">The Tidy Lantern</span>
      </div>
      <ul class="contact-list">
        <li>0438 907 516</li>
        <li>miles@tidylantern.com.au</li>
        <li>PO Box 43 - Brackton, NSW 2187</li>
      </ul>
    </section>
  </main>
</body>
</html>
```